Specialist Technical Theatre service for schools

The task is to design a brochure (A5, 4 pages) for mailing to secondary/high school heads and drama departments to sell them our services as Technical Theatre and Drama professionals who can help them to offer elements of a curriculum that they do not currently offer as well as raise the technical standards of their school productions.
Please find a document attached which outlines the content for the brochure. Please read the document first so that you understand our aims. The text highlighted in yellow takes priority - the text highlighted in blue could be used if there is space.
Photos which may be used available on https://www.pictaro.com/photos/ben_tovey/ (please do not use watermarked nordel images).
Logo is attached (two variants) - one of which should appear somewhere on the design. Website address is www.bentovey.co.uk and email is info@bentovey.co.uk
Target Market(s)
Theatre and Drama teachers in Secondary/High schools
Headteachers of Secondary/High Schools
Industry/Entity Type
Education
Look and feel

```html
<!DOCTYPE html>
<html lang="en">
<head>
<meta charset="utf-8">
<title>Technical Theatre for Schools – Brochure Spread</title>
<link href="https://fonts.googleapis.com/css2?family=Open+Sans:wght@400;600;700&display=swap" rel="stylesheet">
<style>
  :root {
    --backdrop: #b9d4dd;
    --night: #0d0f17;
    --stage-blue: #2b3650;
    --gold: #8c7648;
    --slate: #5c6b96;
    --ink: #ffffff;
    --ink-soft: #e6e8ee;
  }
  * { box-sizing: border-box; margin: 0; padding: 0; }
  html, body { width: 1200px; height: 789px; overflow: hidden; }
  body {
    position: relative;
    background: var(--backdrop);
    font-family: "Open Sans", Arial, sans-serif;
    color: var(--ink);
  }
  .spread {
    position: absolute;
    left: 70px; top: 20px;
    width: 1060px; height: 749px;
    display: flex;
    overflow: hidden;
    box-shadow: 0 10px 30px rgba(20, 40, 60, .35);
  }
  .stage-photo {
    position: absolute; inset: 0;
    background:
      radial-gradient(ellipse 30% 18% at 50% 40%, rgba(170,180,200,.55), transparent 70%),
      radial-gradient(ellipse 45% 25% at 50% 48%, rgba(90,100,125,.6), transparent 75%),
      linear-gradient(180deg, var(--stage-blue) 0%, #1c2232 30%, #161a26 55%, var(--night) 100%);
  }
  .page {
    position: relative;
    width: 530px; height: 749px;
  }
  .page--left { box-shadow: inset -18px 0 22px -16px rgba(0,0,0,.7); }
  .page--right { box-shadow: inset 18px 0 22px -16px rgba(0,0,0,.7); }

  .gold-panel {
    position: absolute;
    background: var(--gold);
    padding: 14px 22px;
    font-size: 12px;
    line-height: 1.36;
  }
  .gold-panel h2 { font-size: 13px; font-weight: 700; margin-bottom: 2px; }
  .roles { list-style: none; }
  .roles li { padding-left: 16px; position: relative; }
  .roles li::before {
    content: ""; position: absolute; left: 0; top: 5px;
    width: 7px; height: 7px; background: var(--ink);
  }
  .roles strong { font-weight: 700; }
  .roles .note { display: block; }

  .panel--roles { left: 40px; top: 60px; width: 440px; }
  .panel--criteria {
    left: 40px; top: 250px; width: 440px;
    padding: 10px 22px;
    font-size: 13px; font-weight: 700;
  }

  .criteria {
    position: absolute; left: 58px; top: 320px; width: 420px;
    font-size: 12px; line-height: 1.36; color: var(--ink-soft);
  }
  .criteria p { margin-bottom: 8px; }

  .budget-tab {
    position: absolute; left: 60px; top: 70px;
    background: var(--slate);
    font-size: 11px; font-weight: 600; letter-spacing: .02em;
    padding: 4px 14px 4px 12px;
  }
  .panel--budget { left: 60px; top: 94px; width: 430px; }

  .pitch {
    position: absolute; left: 60px; top: 320px; width: 430px;
    font-size: 11.5px; line-height: 1.35;
  }
  .pitch h3 { font-size: 12px; font-weight: 700; margin-bottom: 7px; }
  .pitch p { margin-bottom: 6px; color: var(--ink-soft); }
  .pitch .roles { margin-bottom: 9px; color: var(--ink-soft); }
</style>
</head>
<body>
  <div class="spread">
    <div class="stage-photo" role="img" aria-label="Dark concert stage with spotlights and a silhouetted crowd of students with raised arms in haze"></div>

    <section class="page page--left">
      <div class="gold-panel panel--roles">
        <h2>A GCSE or A-Level performance group can comprise of:</h2>
        <ul class="roles">
          <li><strong>Directing</strong> (one candidate per group)</li>
          <li><strong>Acting</strong> (at least two candidates per group)</li>
          <li><strong>Costume design</strong> (one candidate per group)</li>
          <li><strong>Mask design</strong> (one candidate per group)</li>
          <li><strong>Set design</strong> (one candidate per group)</li>
          <li><strong>Technical elements: Lighting and/or Sound</strong>
            <span class="note">(one candidate per element or one candidate assuming responsibility for both elements)</span></li>
        </ul>
      </div>

      <div class="gold-panel panel--criteria">
        You would like someone with the specialist knowledge to ensure that your students meet the assessment criteria?
      </div>

      <div class="criteria">
        <p>“Final lighting design incorporating grid plans and a lantern schedule that indicates the use of at least four different lighting states”</p>
        <p>“The student must supervise the production of the final sound design which they have created and recorded using live and/or sampled material as appropriate”</p>
        <p>“Final costume designs for two characters in the production, incorporating hair, makeup and mask considerations if appropriate. All sourcing must be based wholly on the student’s design(s)”</p>
        <p>“Develop the ability to ensure colour gels, filters, gauzes, silhouettes, projections are used effectively”</p>
        <p>“Develop the ability to ensure sound levels, reverb, echo, recorded sound effects, fades, soundscapes or music are manipulated effectively”</p>
        <p>“Develop the ability to select and exploit appropriate staging forms and to maximise the effectiveness of selected space, use of scale and levels, perspective; configuration of performer/audience relationship”</p>
        <p>And of course through all of the course detail it is repeated that we must “adopt the latest safe working practices.”</p>
      </div>
    </section>

    <section class="page page--right">
      <div class="budget-tab">BUDGET TIGHT?</div>
      <div class="gold-panel panel--budget">
        <p>From £250 to £380 per day* depending on the requirement we are experts at working to academic budgets. We will always deliver the aims of the course using your school and department equipment; however, in order to ensure that your students are familiar with the latest technology we do include any specialist equipment (i.e LED lighting, Motif editing suite, smoke machines etc.) within the cost.</p>
        <p>* discount available if booking consecutive days, mileage charges apply.</p>
      </div>

      <div class="pitch">
        <h3>Your School and Drama Department owns a wide range of technical theatre equipment that isn’t used to its full potential?</h3>
        <h3>You have a school wide musical, play or dance performance approaching and would like to get a student crew motivated, trained and involved in the technical aspects of the performance?</h3>
        <p>If your answer to any of the above is ‘yes’ then we can help.</p>
        <ul class="roles">
          <li>ClearCheck vetted staff (subscribed to the ClearCheck update service so you can run an instant check on our arrival)</li>
          <li>Qualified in Technical Theatre (through a Stage Skills Council accredited establishment)</li>
          <li>SafeWork certified (we adopt the latest safe working practice)</li>
          <li>First Aid Qualified (just in case!)</li>
          <li>Experience of working with Children and Young People in Education (includes previous experience of teaching production skills to GCSE and A-Level students and Youth theatre)</li>
          <li>Currently working in the Theatre and Events Industry (we bring current industry knowledge to you and your students)</li>
        </ul>
        <p>Whether its technical assistance with a one-off school production, practical examination performance support, weekly Technical Theatre Design curriculum delivery or workshops introducing Year 9 to the opportunities offered through Drama GCSE we can help you to find a solution.</p>
      </div>
    </section>
  </div>
</body>
</html>
```